Anzeigengestaltung für KFZ-Werkstatt
Zielgruppe
Wir sind eine KFZ-Werkstatt mit vielumfänglichen Dienstleistungen. Unsere Zielgruppe beschränkt sich auf einen Umkreis von ca. 10km. Wir bieten alles rund ums KFZ: Service, Inspektion, Reparaturen aller Art, TÜV, Rad/Reifen/Felgen, Spurvermessung, Unfallinstandsetzung.
Aufgabenstellung
wir nutzen den Hashtag '#wagenhofmoosl' für Werbung im Internet sowie in den Werbeanzeigen. Wir verwenden diesen 'Slogan' in der SChriftart 'Hashtag', diese kann überall runtergeladen werden. dieser muss in den Werbeanzeigen nicht im Vordergrund stehen, da hier die Zielgruppe eher in Richtung 40+ geht.
es muss auch Platz für die offizielle Firmierung samt Anschrift, Telefon und Internet sein (kein Fax).
was die Anzeige an sich angeht, so sollte das Motiv (gerne erst mal einfach ein Stockfoto) durch uns austauschbar sein. Sprich: wenn Reifensaison ist, wollen wir da ein eigenes Motiv reinstecken können; im Sommer wiederum ein anderes etc. Zudem verwenden wir auch Standardfotos von unserem Unternehmen, welches wir platzieren lassen wenn ein Monat mal nichts besonderes ansteht (die Werbung wird monatlich geschaltet).
Maße: 172x100mm
Hauptfarben (bedingt durch das System, an das wir angeschlossen sind):
ROT: C15 M100 Y100 K0 (oder HKS15; oder Pantone 1797)
GRAU: C0 M0 Y0 K50 (oder 50% HKS90; oder Pantone Cool Gray 7)
Aufgrund der Zielgruppe haben wir als Wunsch 'erschwinglich' angegeben. Dies soll aber nicht heißen, dass wir nicht bereit sind, für das Erstellen der Anzeige kein Geld auszugeben. Nein, damit wollen wir unterstreichen, dass es nicht irre aufgepusht sein soll mit wahnsinns-Effekten etc.

```html
<!DOCTYPE html>
<html lang="de">
<head>
<meta charset="utf-8">
<title>Anzeigen Wagenhof Moosl</title>
<link href="https://fonts.googleapis.com/css2?family=Caveat:wght@500&family=Oswald:wght@200;500&display=swap" rel="stylesheet">
<style>
  :root {
    --stage: #aaa7a8;
    --brand-red: #b01c1f;
    --line-red: #c4161c;
    --ink: #111111;
    --ink-red: #3a0a0b;
    --paper: #ffffff;
    --night: #1c1d20;
  }
  * { margin: 0; padding: 0; box-sizing: border-box; }
  html, body { width: 1200px; height: 1182px; overflow: hidden; background: var(--stage); }
  .stage { position: relative; width: 1200px; height: 1182px; }
  .ad {
    position: absolute; left: 305px; width: 597px; height: 283px;
    overflow: hidden; background: var(--night);
  }
  .ad--spring { top: 94px; }
  .ad--tyres { top: 434px; }
  .ad--lights { top: 773px; }
  .ad__motif { position: absolute; inset: 0; }
  .ad--spring .ad__motif {
    background: radial-gradient(ellipse at 30% 20%, #3d444c 0%, #23272c 45%, #1b1c1f 80%);
  }
  .ad--tyres .ad__motif {
    background:
      radial-gradient(ellipse at 88% 20%, #4a1418 0%, rgba(74,20,24,0) 30%),
      radial-gradient(circle at 30% 75%, #6a7280 0%, #2b3038 40%, #15171b 75%);
  }
  .ad--lights .ad__motif {
    background:
      radial-gradient(ellipse at 25% 30%, #a0754a 0%, #5b4128 28%, rgba(20,20,22,0) 55%),
      #0f0f11;
  }
  .ad__wave { position: absolute; left: 0; top: 0; width: 597px; height: 283px; }
  .ad__badge {
    position: absolute; left: 399px; top: 0; width: 163px; height: 92px;
    background: var(--brand-red);
  }
  .ad__hashtag {
    position: absolute; left: 372px; top: 16px; width: 210px;
    font-family: "Caveat", cursive; font-weight: 500; font-size: 38px;
    color: var(--paper); line-height: 1; white-space: nowrap;
  }
  .ad__url {
    position: absolute; left: 399px; top: 66px; width: 163px; text-align: center;
    font-family: "Oswald", sans-serif; font-weight: 500; font-size: 11px;
    letter-spacing: 2.6px; color: var(--ink-red);
  }
  .ad__headline {
    position: absolute; left: 34px; top: 72px;
    font-family: "Caveat", cursive; font-weight: 500; font-size: 44px;
    color: var(--paper); line-height: 1; white-space: nowrap;
  }
  .ad__offer {
    position: absolute; left: 34px; top: 122px;
    font-family: "Oswald", sans-serif; font-weight: 200; font-size: 19px;
    color: #e6e6e6; line-height: 1; white-space: nowrap; letter-spacing: -0.3px;
  }
  .ad__offer strong { font-weight: 500; color: var(--paper); }
  .ad__contact {
    position: absolute; left: 420px; top: 191px; width: 160px;
    font-family: "Oswald", sans-serif; font-weight: 500; font-size: 12.5px;
    line-height: 18px; color: var(--ink); text-align: center; text-transform: uppercase;
    font-style: normal;
  }
</style>
</head>
<body>
<div class="stage">

  <section class="ad ad--spring">
    <div class="ad__motif" role="img" aria-label="Foto: gesteppter dunkler Ledersitz im Fahrzeuginnenraum"></div>
    <svg class="ad__wave" viewBox="0 0 962 457" preserveAspectRatio="none" aria-hidden="true">
      <path d="M0 390 C90 360 170 340 260 345 C360 350 420 385 490 382 C590 378 680 290 800 272 C880 262 930 295 962 320 L962 457 L0 457 Z" fill="var(--paper)"/>
      <path d="M0 405 C120 375 230 355 330 358 C420 361 470 378 530 372 C620 360 700 275 810 262 C880 255 930 285 962 305" fill="none" stroke="var(--line-red)" stroke-width="1.6"/>
    </svg>
    <div class="ad__badge"></div>
    <div class="ad__hashtag">#wagenhofmoosl</div>
    <div class="ad__url">WAGENHOF-MOOSL.DE</div>
    <h2 class="ad__headline">Frühjahrsputz</h2>
    <p class="ad__offer">INNENRAUM-REINIGUNG AB <strong>X,XX €</strong></p>
    <address class="ad__contact">Moosweg 12<br>93199 Musterbach<br>+49 1234 567890<br>info@wagenhof-moosl.de</address>
  </section>

  <section class="ad ad--tyres">
    <div class="ad__motif" role="img" aria-label="Foto: Sportfelge mit Reifen und Bremsscheibe"></div>
    <svg class="ad__wave" viewBox="0 0 962 457" preserveAspectRatio="none" aria-hidden="true">
      <path d="M0 390 C90 360 170 340 260 345 C360 350 420 385 490 382 C590 378 680 290 800 272 C880 262 930 295 962 320 L962 457 L0 457 Z" fill="var(--paper)"/>
      <path d="M0 405 C120 375 230 355 330 358 C420 361 470 378 530 372 C620 360 700 275 810 262 C880 255 930 285 962 305" fill="none" stroke="var(--line-red)" stroke-width="1.6"/>
    </svg>
    <div class="ad__badge"></div>
    <div class="ad__hashtag">#wagenhofmoosl</div>
    <div class="ad__url">WAGENHOF-MOOSL.DE</div>
    <h2 class="ad__headline">Winterstiefel gefällig?</h2>
    <p class="ad__offer">WINTERREIFEN WECHSEL AB <strong>X,XX €</strong></p>
    <address class="ad__contact">Moosweg 12<br>93199 Musterbach<br>+49 1234 567890<br>info@wagenhof-moosl.de</address>
  </section>

  <section class="ad ad--lights">
    <div class="ad__motif" role="img" aria-label="Foto: Frontscheinwerfer eines bronzefarbenen Autos im Dunkeln"></div>
    <svg class="ad__wave" viewBox="0 0 962 457" preserveAspectRatio="none" aria-hidden="true">
      <path d="M0 390 C90 360 170 340 260 345 C360 350 420 385 490 382 C590 378 680 290 800 272 C880 262 930 295 962 320 L962 457 L0 457 Z" fill="var(--paper)"/>
      <path d="M0 405 C120 375 230 355 330 358 C420 361 470 378 530 372 C620 360 700 275 810 262 C880 255 930 285 962 305" fill="none" stroke="var(--line-red)" stroke-width="1.6"/>
    </svg>
    <div class="ad__badge"></div>
    <div class="ad__hashtag">#wagenhofmoosl</div>
    <div class="ad__url">WAGENHOF-MOOSL.DE</div>
    <h2 class="ad__headline">Schlechte Sicht?</h2>
    <p class="ad__offer">LICHT-TEST AB <strong>X,XX €</strong></p>
    <address class="ad__contact">Moosweg 12<br>93199 Musterbach<br>+49 1234 567890<br>info@wagenhof-moosl.de</address>
  </section>

</div>
</body>
</html>
```